Label Design for a sexy ladies 5 pocket skinny

We need modern packaging design for women's skinny 5 pocket pants for a brand name Quill. All kinds of packaging designs are welcome.
The pant is folded and packaged in a poly bag. We require a label design for the brand name Quill. The main label will be attached by a string on the belt loop. the size of that label will 25cm in length and 10cm wide. This is the first label the customer see's when she picks up the garment. Therefore, we require an eye catching design for that. If required it could have certain information about the pant on the main label such as Comfort fit, Wrinkle-resistant, machine washable, luxury fabric. But, if you feel that adding the above information spoils the design of the label then it is not a must to include the above information. On the back of the label we like to include the information that this pant was manufactured in an Terravo Gold certified green plant and hence the damage to the environment because of the plant is nill.
The second label is attached on to the waist band and the purpose of that label is to include the size of the pant such 32x32. The size of that label is 8cm in length and 4cm in width. There is no design on the back on this label it has to be blank.
Sample is given for what we currently use for our mens chino pant. we are looking for something very different.
Reason: because there was a delay in the project being approved by pixel harbor.

```html
<!DOCTYPE html>
<html lang="en">
<head>
<meta charset="utf-8">
<title>Quill – Ladies Skinny Label Set</title>
<link href="https://fonts.googleapis.com/css2?family=Oswald:wght@500;700&family=Josefin+Sans:wght@300;400;600&display=swap" rel="stylesheet">
<style>
  :root {
    --bg-light: #f2f2f3;
    --bg-shade: #d2d3d6;
    --navy: #141a4a;
    --navy-deep: #0d1236;
    --ink-white: #ffffff;
    --rule: rgba(255,255,255,0.85);
    --hole: #f2f2f3;
    --forest: #2f5a2a;
    --meadow: #8fbf4a;
    --sky: #bfe3ec;
    --lake: #3c8fa6;
  }
  * { box-sizing: border-box; margin: 0; padding: 0; }
  html, body { width: 1200px; height: 1000px; overflow: hidden; }
  body {
    background: radial-gradient(ellipse at 50% 45%, var(--bg-light) 0%, var(--bg-light) 45%, var(--bg-shade) 100%);
    font-family: "Josefin Sans", sans-serif;
    color: var(--ink-white);
    position: relative;
  }

  .tag {
    position: absolute;
    width: 260px;
    height: 650px;
    border-radius: 4px;
    overflow: hidden;
    box-shadow: 0 8px 22px rgba(0,0,0,0.22);
  }
  .tag-hole {
    position: absolute;
    top: 22px; left: 50%;
    width: 18px; height: 18px;
    margin-left: -9px;
    border-radius: 50%;
    background: var(--hole);
    border: 3px solid #c9a25a;
    z-index: 3;
  }

  /* Hang tag – back */
  .tag-back {
    left: 140px; top: 175px;
    background: var(--navy);
    display: flex; flex-direction: column; align-items: center;
    padding: 60px 22px 26px;
  }
  .product-line {
    display: flex; align-items: center; gap: 10px;
    font-weight: 400; font-size: 15px; letter-spacing: 2px;
    text-transform: uppercase; text-align: center; line-height: 1.2;
  }
  .chevrons { width: 22px; height: 12px; }
  .garment-flats {
    width: 216px; height: 250px; margin-top: 18px;
    background: linear-gradient(180deg, #1b2258 0%, #1d2a55 70%, #2a3d3a 100%);
    border: 1px solid rgba(255,255,255,0.25);
  }
  .feature-list { list-style: none; margin-top: 22px; text-align: center; width: 100%; }
  .feature-list li {
    font-weight: 600; font-size: 14px; letter-spacing: 1.5px; text-transform: uppercase;
    padding: 5px 0; border-top: 1px solid var(--rule);
  }
  .feature-list li:last-child { border-bottom: 1px solid var(--rule); }
  .dots { margin-top: 16px; font-size: 14px; letter-spacing: 6px; }
  .eco-note {
    margin-top: 8px; font-size: 12px; font-weight: 300; line-height: 1.35;
    text-transform: uppercase; letter-spacing: 1.5px; text-align: justify; text-align-last: center;
  }

  /* Hang tag – front */
  .tag-front { left: 470px; top: 175px; }
  .scenery {
    position: absolute; inset: 0;
    background: linear-gradient(180deg, var(--sky) 0%, #e8f3d8 22%, var(--meadow) 42%, var(--forest) 60%, var(--lake) 78%, var(--meadow) 100%);
  }
  .brand-name {
    position: absolute; left: 28px; top: 70px;
    writing-mode: vertical-rl; transform: rotate(180deg);
    font-family: "Oswald", sans-serif; font-weight: 700; font-size: 62px;
    letter-spacing: 4px; text-transform: uppercase; color: var(--ink-white);
  }
  .front-product-line {
    position: absolute; left: 20px; top: 440px; width: 230px;
    transform: rotate(-14deg);
    display: flex; align-items: center; gap: 8px;
    font-weight: 600; font-size: 16px; letter-spacing: 1.5px; text-transform: uppercase;
    line-height: 1.15; color: var(--ink-white); text-shadow: 0 1px 2px rgba(0,0,0,0.35);
  }

  /* Size labels */
  .size-label {
    position: absolute; background: var(--navy-deep);
    box-shadow: 0 6px 16px rgba(0,0,0,0.2);
    font-family: "Oswald", sans-serif;
  }
  .size-label::after {
    content: ""; position: absolute; inset: 6px;
    border: 1px dashed rgba(255,255,255,0.7);
  }
  .size-wide {
    left: 820px; top: 200px; width: 220px; height: 110px;
    display: flex; align-items: center; justify-content: center; gap: 8px;
  }
  .size-num { font-weight: 500; font-size: 54px; line-height: 1; }
  .size-x { font-size: 24px; }
  .size-caption {
    font-family: "Josefin Sans", sans-serif; font-size: 9px; font-weight: 600;
    letter-spacing: 1px; text-transform: uppercase;
    writing-mode: vertical-rl; transform: rotate(180deg);
  }
  .size-tall {
    left: 875px; top: 400px; width: 110px; height: 220px;
    display: flex; flex-direction: column; align-items: center; justify-content: center; gap: 2px;
  }
  .size-tall .size-caption { writing-mode: horizontal-tb; transform: none; font-size: 11px; }
</style>
</head>
<body>

  <article class="tag tag-back" aria-label="Hang tag, back side">
    <span class="tag-hole"></span>
    <div class="product-line">
      <svg class="chevrons" viewBox="0 0 22 12"><path d="M7 1 L2 6 L7 11 M13 1 L8 6 L13 11" fill="none" stroke="#fff" stroke-width="1.5"/></svg>
      <span>Ladies Skinny<br>5 Pocket Pants</span>
    </div>
    <div class="garment-flats" role="img" aria-label="Front and back line drawing of the skinny pants"></div>
    <ul class="feature-list">
      <li>Comfort Fit</li>
      <li>Wrinkle-Resistant</li>
      <li>Machine Washable</li>
      <li>Luxury Fabric</li>
    </ul>
    <div class="dots">•••</div>
    <p class="eco-note">This Quill skinny was proudly produced in a Terravo Gold certified green plant with no negative environmental impact.</p>
    <div class="dots">•••</div>
  </article>

  <article class="tag tag-front" aria-label="Hang tag, front side">
    <div class="scenery" role="img" aria-label="Photo of a forest lake landscape with a grazing moose"></div>
    <span class="tag-hole"></span>
    <h1 class="brand-name">Quill</h1>
    <div class="front-product-line">
      <svg class="chevrons" viewBox="0 0 22 12"><path d="M7 1 L2 6 L7 11 M13 1 L8 6 L13 11" fill="none" stroke="#fff" stroke-width="1.5"/></svg>
      <span>Ladies Skinny<br>5 Pocket Pants</span>
      <svg class="chevrons" viewBox="0 0 22 12"><path d="M9 1 L14 6 L9 11 M15 1 L20 6 L15 11" fill="none" stroke="#fff" stroke-width="1.5"/></svg>
    </div>
  </article>

  <section class="size-label size-wide" aria-label="Size label, horizontal">
    <span class="size-caption">Waist</span>
    <span class="size-num">32</span>
    <span class="size-x">x</span>
    <span class="size-num">32</span>
    <span class="size-caption">Length</span>
  </section>

  <section class="size-label size-tall" aria-label="Size label, vertical">
    <span class="size-num">32</span>
    <span class="size-caption">Waist</span>
    <span class="size-x">x</span>
    <span class="size-num">32</span>
    <span class="size-caption">Length</span>
  </section>

</body>
</html>
```